The Lumo-Hub for Rescue Instruction + Venue Readiness Post Card

Hi! I am a new business that is Licensed Training Provider to the National Bluefield Aid. We teach private CPR/AED, First Aid and a variety of other emergency training courses to the general public! Our goal is to get into businesses of all sizes from the mom and pops store to corporate offices of Manhattan. We can do private classes in your home and no office space is to small! We even have a school assembly program that teaches "Hands Only CPR" for children. I'm looking to make a post card to hand out that can easily explain what we are doing…that might have some good visuals that catch your eye as well. I def want to use The Lumo Hub logo in it that I have attached. Im not necessarily married to any of the other images. You can check out our website www.lumohubinstruct.example for more information and you can use any of the images on there as well if you would like. I will give you free reign to find any cool photo stock image that you might think fits with what I'm trying to do. Hopefully you can help!
Updates

Also feel free to use any other photos that you might find that you think fit our cause for teaching CPR/First aid etc!! Thanks!

Thank you all for your hard work. I actually like many of these designs and really torn! I will be making some decisions in the next day or so. Thank you! Dale

Industry/Entity Type

Training

```html
<!DOCTYPE html>
<html lang="en">
<head>
<meta charset="utf-8">
<title>The Lumo Hub – Post Card</title>
<link href="https://fonts.googleapis.com/css2?family=Oswald:wght@500;700&family=Open+Sans:wght@400;600;700&display=swap" rel="stylesheet">
<style>
  :root {
    --bg: #f1f1f1;
    --paper: #ffffff;
    --paper-shade: #e6e7e8;
    --red: #d7141d;
    --charcoal: #2b2b2d;
    --steel: #4a4b4e;
    --silver: #b7b8bb;
    --text: #333335;
    --muted: #6a6b6e;
  }
  * { box-sizing: border-box; margin: 0; padding: 0; }
  html, body { width: 1200px; height: 900px; overflow: hidden; }
  body {
    background: var(--bg);
    font-family: "Open Sans", Arial, sans-serif;
    color: var(--text);
    position: relative;
  }
  .postcard {
    position: absolute;
    top: 263px;
    width: 560px;
    height: 374px;
    background: var(--paper);
    box-shadow: 0 6px 18px rgba(0,0,0,.15);
    overflow: hidden;
  }
  .postcard--back { left: 30px; }
  .postcard--front { left: 610px; }
  .postcard__art { position: absolute; inset: 0; width: 100%; height: 100%; }

  .brand {
    display: flex;
    align-items: center;
    gap: 6px;
    font-family: "Open Sans", Arial, sans-serif;
    font-weight: 400;
    color: var(--charcoal);
    letter-spacing: .5px;
  }
  .brand__dot {
    width: 12px; height: 12px;
    border-radius: 50%;
    background: var(--red);
    flex: none;
  }

  /* Front */
  .front-brand { position: absolute; left: 34px; top: 302px; font-size: 22px; }
  .headline {
    position: absolute; left: 290px; top: 280px;
    font-family: "Oswald", Impact, sans-serif;
    font-weight: 700;
    line-height: .95;
    text-transform: uppercase;
  }
  .headline__ready { font-size: 27px; color: var(--charcoal); }
  .headline__small { font-size: 12px; color: var(--charcoal); }
  .headline__emergency { font-size: 27px; color: var(--red); }
  .headline__mark { font-size: 46px; color: var(--charcoal); vertical-align: -2px; }
  .headline__tag { font-size: 15px; color: var(--charcoal); margin-left: 4px; }

  /* Back */
  .back-copy { position: absolute; left: 298px; top: 16px; width: 246px; }
  .back-brand { font-size: 19px; justify-content: flex-end; margin-bottom: 8px; }
  .intro { font-size: 10px; font-weight: 700; line-height: 1.3; margin-bottom: 7px; }
  .services__title {
    font-family: "Oswald", Impact, sans-serif;
    font-weight: 700; font-size: 13px; line-height: 1.2; text-transform: uppercase; color: var(--charcoal);
  }
  .services__list { list-style: none; font-size: 8.2px; line-height: 1.3; color: var(--muted); margin: 2px 0 7px; }
  .training {
    font-family: "Oswald", Impact, sans-serif;
    font-weight: 700; text-transform: uppercase; color: var(--charcoal); line-height: 1.05;
  }
  .training__title { font-size: 16px; }
  .training__list { font-size: 10.5px; font-weight: 500; }
  .contact {
    position: absolute; right: 16px; bottom: 12px;
    font-size: 8.5px; line-height: 1.35; color: var(--muted); text-align: right;
  }
</style>
</head>
<body>

  <section class="postcard postcard--back">
    <svg class="postcard__art" viewBox="0 0 560 374">
      <defs>
        <linearGradient id="trainee-photo" x1="0" y1="0" x2="1" y2="1">
          <stop offset="0" stop-color="#5a1f25"/>
          <stop offset=".5" stop-color="#3c4fa8"/>
          <stop offset="1" stop-color="#d8c8a8"/>
        </linearGradient>
      </defs>
      <path d="M196,0 C280,90 280,290 218,374 H240 C300,290 300,90 214,0 Z" fill="var(--silver)"/>
      <path d="M180,0 C260,90 260,290 200,374 H218 C280,290 280,90 196,0 Z" fill="var(--red)"/>
      <path d="M0,0 H180 C260,90 260,290 200,374 H0 Z" fill="url(#trainee-photo)" role="img" aria-label="Photo: hands using a bag-valve rescue mask on a CPR training manikin"/>
    </svg>
    <div class="back-copy">
      <div class="brand back-brand"><span>the lumo hub</span><span class="brand__dot"></span></div>
      <p class="intro">The Lumo-Hub is a leading Provider of safety and emergency preparedness training + venue readiness management.</p>
      <h3 class="services__title">Services we provide:</h3>
      <ul class="services__list">
        <li>-National Certification in a variety of CPR/AED/First Aid/O2 Courses</li>
        <li>-National Bluefield Aid Lifeguard Training</li>
        <li>-Standby Ambulances Paramedics/EMTs</li>
        <li>-Lifeguards for all events</li>
        <li>-Rescue Boat Rentals</li>
        <li>-Marine Safety Coordination</li>
        <li>-Certified Rescue Divers</li>
        <li>-Communication Rentals</li>
        <li>-Customized Emergency Action Plans</li>
        <li>-First Aid Kits/Supplies</li>
        <li>-Athletic Trainers</li>
        <li>-Safety walk throughs</li>
        <li>-Fireguards</li>
      </ul>
      <div class="training">
        <div class="training__title">Training</div>
        <div class="training__list">CPR, First Aid, Emergency Response</div>
      </div>
    </div>
    <address class="contact">
      Dale Ashworth<br>
      555 010 4821<br>
      lumohub911@mailbox.example<br>
      www.lumohubinstruct.example
    </address>
  </section>

  <section class="postcard postcard--front">
    <svg class="postcard__art" viewBox="0 0 560 374">
      <defs>
        <linearGradient id="card-fade" x1="0" y1="0" x2="0" y2="1">
          <stop offset="0" stop-color="var(--paper)"/>
          <stop offset="1" stop-color="var(--paper-shade)"/>
        </linearGradient>
        <linearGradient id="class-photo" x1="0" y1="0" x2="1" y2="0">
          <stop offset="0" stop-color="#dfe3e8"/>
          <stop offset=".55" stop-color="#2f63b8"/>
          <stop offset="1" stop-color="#e8eaec"/>
        </linearGradient>
      </defs>
      <rect width="560" height="374" fill="url(#card-fade)"/>
      <path d="M0,262 C360,262 510,170 560,40 V130 C500,240 330,300 0,304 Z" fill="#d4d5d7"/>
      <path d="M0,252 C350,250 500,140 548,0 H560 V40 C510,170 360,262 0,262 Z" fill="var(--steel)"/>
      <path d="M0,240 C330,230 470,120 520,0 H548 C500,140 350,250 0,252 Z" fill="var(--red)"/>
      <path d="M0,0 H520 C470,120 330,230 0,240 Z" fill="url(#class-photo)" role="img" aria-label="Photo: an instructor guiding a trainee doing chest compressions on a CPR manikin"/>
    </svg>
    <div class="brand front-brand"><span>the lumo hub</span><span class="brand__dot"></span></div>
    <h2 class="headline">
      <span class="headline__ready">Ready</span> <span class="headline__small">for an</span><br>
      <span class="headline__emergency">Emergency</span><span class="headline__mark">?</span><span class="headline__tag">You can be</span>
    </h2>
  </section>

</body>
</html>
```